The hardcover "Crimson Register" (large size, Quarto 4º, 12 × 9 1/2 in, 30.5 × 24.15 cm) in German language as follows:

PURPURNES REGISTER (title)
der herausragendsten Unternehmer und Manager Deutschlands 2013 (subtitle 1)
BERLIN UND BRANDENBURG (subtitle 2, smaller than subtitle 1)

Quorvexa (logo, WMF file attached)

Reason: The solutions are rather too childish and pre-made styles... is there anyone who can make it better? - a professional-looking business book (encyclopedia style, should have no color-pictures, no author's name, logo smaller due to the large size book)

Target Market(s)

business community

Requirements
Must have
• encyclopedia style large size book
must look professional and expensive

Nice to have
• - gold-color hardcover, or some gold-color elements
- some simple and decent graphic element (e.g. an ancient column, or some other architectural detail), if any
Should not have
• no color-pictures
no author's name

```html
<!DOCTYPE html>
<html lang="de">
<head>
<meta charset="utf-8">
<title>Purpurnes Register 2013 – Cover</title>
<link rel="stylesheet" href="https://fonts.googleapis.com/css2?family=Roboto:wght@300;400;700&display=swap">
<style>
  :root {
    --paper: #ffffff;
    --board: #000000;
    --gold: #f39200;
    --ink: #1a1a1a;
  }
  html, body {
    margin: 0;
    padding: 0;
    width: 1081px;
    height: 1200px;
    overflow: hidden;
    background: var(--paper);
  }
  .cover-sheet {
    display: block;
    width: 1081px;
    height: 1200px;
  }
  .board { fill: var(--board); }
  .gold-type {
    fill: var(--gold);
    font-family: "Roboto", Arial, sans-serif;
    font-weight: 700;
  }
  .option-label {
    fill: var(--ink);
    font-family: "Roboto", Arial, sans-serif;
    font-weight: 300;
    font-size: 34px;
  }
  .column-area { fill: var(--gold); }
  .imprint-mark { fill: var(--gold); }
</style>
</head>
<body>
<svg class="cover-sheet" viewBox="0 0 1081 1200" xmlns="http://www.w3.org/2000/svg">
  <g class="front-cover">
    <rect class="board" x="52" y="0" width="841" height="1133"/>

    <text class="gold-type title-line" x="81" y="157" font-size="140" textLength="731" lengthAdjust="spacingAndGlyphs">PURPURNES</text>
    <text class="gold-type title-line" x="81" y="268" font-size="140" textLength="731" lengthAdjust="spacingAndGlyphs">REGISTER 2013</text>

    <text class="gold-type subtitle-line" x="81" y="378" font-size="62" textLength="728" lengthAdjust="spacingAndGlyphs">DER HERAUSRAGENDSTEN</text>
    <text class="gold-type subtitle-line" x="81" y="444" font-size="76" textLength="728" lengthAdjust="spacingAndGlyphs">UNTERNEHMER UND</text>
    <text class="gold-type subtitle-line" x="81" y="509" font-size="62" textLength="728" lengthAdjust="spacingAndGlyphs">MANAGER DEUTSCHLANDS</text>

    <text class="gold-type region-line" x="174" y="598" font-size="43" textLength="546" lengthAdjust="spacingAndGlyphs">BERLIN UND BRANDENBURG</text>

    <rect class="column-area" x="228" y="646" width="464" height="372" rx="6"
          role="img" aria-label="Illustration eines antiken Säulenstumpfs mit Basis in Gold"/>

    <g class="imprint">
      <rect class="imprint-mark" x="688" y="1080" width="18" height="18"/>
      <text class="gold-type" x="712" y="1098" font-size="22" textLength="94" lengthAdjust="spacingAndGlyphs">Quorvexa</text>
    </g>
  </g>

  <g class="spine">
    <rect class="board" x="929" y="0" width="110" height="1133"/>
    <text class="gold-type spine-year" transform="translate(1031,215) rotate(-90)" font-size="76" textLength="165" lengthAdjust="spacingAndGlyphs">2013</text>
    <rect class="column-area" x="962" y="254" width="66" height="98" rx="4"
          role="img" aria-label="Kleine Illustration eines antiken Säulenstumpfs in Gold"/>
    <text class="gold-type spine-title" transform="translate(1031,1012) rotate(-90)" font-size="76" textLength="620" lengthAdjust="spacingAndGlyphs">PURPURNES REGISTER</text>
    <g class="imprint">
      <rect class="imprint-mark" x="946" y="1090" width="11" height="11"/>
      <text class="gold-type" x="961" y="1101" font-size="15" textLength="64" lengthAdjust="spacingAndGlyphs">Quorvexa</text>
    </g>
  </g>

  <text class="option-label" x="7" y="1197">OPTION 1</text>
</svg>
</body>
</html>
```